A land page lead collector for people who want to reduce there postage costs

We are looking to create a single page website landing page to collect leads of people who want to reduce there postage costs.

The form should basically ask:

Name:
Business Name:
Address:
Town:
Post Code:
Email:
Phone:
Letter Volume Per Week:
Parcel Volume Per Week:

We should basically be advertising cheaper postage costs.

We will not be showing prices on this website we will just be collecting the leads.

Our competition website is as follows https://mailfernquest.com

But we are not a online service. This is just a collector to get leads of people who want to save money on there postage costs.
Updates

Target Market(s)

Small and medium sized enterprises

Industry/Entity Type

Advertising

Number of Pages Required

1 page

Colors
ec2027
0356a4

Requirements
Must have
• Form above the fold of the page
Nice to have
• Colour red and blue.
• Parallax design would be nice.

```html
<!DOCTYPE html>
<html lang="en">
<head>
<meta charset="utf-8">
<title>Reduce Your Postage Costs</title>
<link rel="stylesheet" href="https://fonts.googleapis.com/css2?family=Oswald:wght@400;500;600&family=Noto+Sans:wght@400;700&display=swap">
<style>
  :root {
    --red: #ec2027;
    --blue: #0356a4;
    --blue-band: #034a90;
    --blue-card: #0a4a8f;
    --blue-button: #0b4fa0;
    --white: #ffffff;
    --field: #ececec;
    --field-text: #8a8a8a;
    --photo-dark: #3a1a22;
    --photo-mid: #7a2a36;
    --photo-warm: #a8404a;
  }
  * { box-sizing: border-box; margin: 0; padding: 0; }
  html, body { width: 718px; height: 1200px; overflow: hidden; }
  body {
    position: relative;
    background: var(--blue);
    font-family: "Noto Sans", Arial, sans-serif;
    color: var(--white);
  }
  .backdrop { position: absolute; inset: 0; width: 718px; height: 1200px; }
  .abs { position: absolute; }

  .hero-title { top: 48px; left: 0; width: 718px; text-align: center; font-family: "Oswald", sans-serif; text-transform: uppercase; line-height: 1; }
  .hero-title .kicker { display: block; font-size: 19px; font-weight: 400; letter-spacing: .5px; }
  .hero-title .headline { display: block; font-size: 29px; font-weight: 600; margin-top: 4px; }

  .lead-form {
    top: 143px; left: 93px; width: 268px; height: 270px;
    background: rgba(255,255,255,.12);
    border: 2px solid rgba(255,255,255,.35);
    border-radius: 3px;
    box-shadow: 0 8px 10px -6px rgba(0,0,0,.45);
  }
  .field {
    position: absolute; height: 25px;
    background: var(--field); border: 1px solid #d8d8d8; border-radius: 2px;
    font-size: 9.5px; color: var(--field-text); padding: 6px 0 0 6px;
  }
  .field.half-l { left: 10px; width: 117px; }
  .field.half-r { left: 138px; width: 118px; }
  .field.full { left: 10px; width: 246px; }
  .volume-label { position: absolute; left: 15px; font-size: 9.5px; color: var(--white); }
  .volume-select {
    position: absolute; left: 138px; width: 58px; height: 25px;
    background: var(--field); border-radius: 2px; font-size: 9.5px; color: var(--field-text); padding: 6px 0 0 12px;
  }
  .volume-select::after {
    content: ""; position: absolute; right: 7px; top: 10px;
    border-left: 5px solid transparent; border-right: 5px solid transparent; border-top: 5px solid #8a8a8a;
  }
  .submit-button {
    position: absolute; left: 10px; top: 224px; width: 246px; height: 32px;
    background: var(--red); border-radius: 2px; text-align: center;
    font-family: "Oswald", sans-serif; font-weight: 500; font-size: 15px; line-height: 32px;
  }

  .section-title { font-family: "Oswald", sans-serif; font-weight: 400; font-size: 21px; text-transform: uppercase; line-height: 1; }
  .about-title { top: 443px; left: 99px; }
  .about-copy { top: 478px; left: 99px; width: 528px; font-size: 10.4px; line-height: 17px; }

  .video-player { top: 615px; left: 99px; width: 313px; height: 182px; overflow: hidden; }
  .video-still { position: absolute; inset: 0; background: linear-gradient(100deg, var(--photo-mid), var(--photo-warm) 45%, #c69a94 80%, #b6857f); }
  .video-action { position: absolute; right: 7px; width: 24px; height: 18px; background: rgba(30,30,30,.85); border-radius: 2px; font-size: 4.5px; font-weight: 700; text-align: center; padding-top: 10px; }
  .video-controls { position: absolute; left: 6px; right: 6px; bottom: 7px; height: 22px; }
  .play-button { position: absolute; left: 0; top: 0; width: 40px; height: 22px; background: rgba(30,30,30,.85); border-radius: 2px; }
  .play-button::after { content: ""; position: absolute; left: 16px; top: 6px; border-top: 5px solid transparent; border-bottom: 5px solid transparent; border-left: 8px solid var(--white); }
  .timeline { position: absolute; left: 46px; right: 0; top: 0; height: 22px; background: rgba(30,30,30,.85); border-radius: 2px; }
  .timeline .track { position: absolute; left: 8px; width: 190px; top: 9px; height: 4px; background: #555; }
  .timeline .played { position: absolute; left: 0; top: 0; width: 88px; height: 4px; background: #1aa6de; }
  .timeline .time { position: absolute; left: 78px; top: -9px; font-size: 6px; background: #222; padding: 0 3px; }
  .timeline .hd { position: absolute; right: 20px; top: 6px; font-size: 7px; font-weight: 700; font-style: italic; color: #1aa6de; }

  .related { top: 624px; left: 441px; width: 180px; }
  .related .section-title { font-size: 14.5px; }
  .related ul { margin-top: 10px; list-style: none; }
  .related li { position: relative; font-size: 8.3px; line-height: 10px; padding-left: 8px; margin-bottom: 7px; }
  .related li::before { content: ""; position: absolute; left: 0; top: 3px; width: 4px; height: 4px; border-radius: 50%; background: var(--white); }

  .steps-title { top: 870px; left: 0; width: 718px; text-align: center; }
  .step-card { top: 924px; width: 162px; height: 92px; background: var(--blue-card); border-radius: 2px; text-align: center; font-size: 8.8px; line-height: 12.3px; padding: 29px 10px 0; }
  .step-number {
    position: absolute; left: 65px; top: -15px; width: 31px; height: 31px; border-radius: 50%;
    background: var(--red); border: 2px solid var(--white); box-shadow: 0 0 0 1px #c7c7c7;
    font-family: "Oswald", sans-serif; font-weight: 500; font-size: 14px; line-height: 27px;
  }

  .newsletter-title { top: 1089px; left: 91px; font-family: "Oswald", sans-serif; font-size: 14px; text-transform: uppercase; }
  .newsletter-title strong { font-weight: 500; }
  .newsletter-title span { font-weight: 400; }
  .newsletter-input { top: 1120px; left: 91px; width: 212px; height: 25px; border-radius: 13px; background: var(--white); color: #9a9a9a; font-size: 9.5px; padding: 6px 0 0 12px; }
  .subscribe-button { top: 1153px; left: 92px; width: 71px; height: 24px; border-radius: 12px; background: var(--blue-button); font-size: 10.5px; text-align: center; line-height: 24px; }
  .social-links { top: 1118px; left: 470px; display: flex; gap: 5px; }
  .social-links span { width: 27px; height: 27px; border-radius: 50%; background: var(--white); display: block; }
  .legal { top: 1157px; left: 471px; font-size: 8px; line-height: 12px; }
  .legal .links span + span::before { content: "•"; margin: 0 6px; }
</style>
</head>
<body>
  <svg class="backdrop" viewBox="0 0 718 1200" aria-hidden="true">
    <defs>
      <linearGradient id="hero-tone" x1="0" y1="0" x2="1" y2="0.4">
        <stop offset="0" stop-color="#5a1f2b"/>
        <stop offset=".35" stop-color="#8a2e3a"/>
        <stop offset=".7" stop-color="#9a4450"/>
        <stop offset="1" stop-color="#6a2a30"/>
      </linearGradient>
    </defs>
    <rect x="0" y="0" width="718" height="410" fill="url(#hero-tone)"/>
    <polygon points="0,350 718,405 718,1200 0,1200" fill="var(--blue)"/>
    <polygon points="0,605 718,562 718,800 0,842" fill="var(--blue-band)"/>
    <polygon points="0,1075 718,1030 718,1200 0,1200" fill="var(--red)"/>
  </svg>
  <div class="abs" role="img" aria-label="Photograph of a hand posting a letter into a red post box" style="top:0;left:0;width:718px;height:350px;"></div>

  <header class="abs hero-title">
    <span class="kicker">Who want to</span>
    <span class="headline">Reduce there postage costs</span>
  </header>

  <form class="abs lead-form">
    <div class="field half-l" style="top:8px">Name</div>
    <div class="field half-r" style="top:8px">Business Name</div>
    <div class="field full" style="top:44px">Address</div>
    <div class="field half-l" style="top:80px">Town</div>
    <div class="field half-r" style="top:80px">Post Code</div>
    <div class="field half-l" style="top:116px">Email</div>
    <div class="field half-r" style="top:116px">Phone</div>
    <div class="volume-label" style="top:159px">Letter Volume Per Week:</div>
    <div class="volume-select" style="top:152px">1</div>
    <div class="volume-label" style="top:195px">Parcel Volume Per Week:</div>
    <div class="volume-select" style="top:188px">1</div>
    <div class="submit-button">SUBMIT</div>
  </form>

  <h2 class="abs section-title about-title">About us</h2>
  <p class="abs about-copy">Lorem ipsum dolor sit amet, consectetur adipiscing elit, sed do eiusmod tempor incididunt ut labore et dolore magna aliqua. Ut enim ad minim veniam, quis nostrud exercitation ullamco laboris nisi ut aliquip ex ea commodo consequat. Duis aute irure dolor in reprehenderit in voluptate velit esse cillum dolore eu fugiat nulla pariatur. Excepteur sint occaecat cupidatat non proident.</p>

  <div class="abs video-player">
    <div class="video-still" role="img" aria-label="Video still of a hand posting a letter into a red post box"></div>
    <div class="video-action" style="top:9px">LIKE</div>
    <div class="video-action" style="top:31px">SHARE</div>
    <div class="video-action" style="top:53px">EMBED</div>
    <div class="video-controls">
      <div class="play-button"></div>
      <div class="timeline">
        <div class="track"><div class="played"></div><span class="time">00:34</span></div>
        <span class="hd">HD</span>
      </div>
    </div>
  </div>

  <aside class="abs related">
    <h3 class="section-title">Related articles</h3>
    <ul>
      <li>Lorem ipsum dolor sit amet, consectetur adipiscing eli</li>
      <li>Lorem ipsum dolor sit amet, consectetur adipiscing eli</li>
      <li>Lorem ipsum dolor sit amet, consectetur adipiscing eli</li>
      <li>Lorem ipsum dolor sit amet, consectetur adipiscing eli</li>
      <li>Lorem ipsum dolor sit amet, consectetur adipiscing eli</li>
    </ul>
  </aside>

  <h2 class="abs section-title steps-title">How it work</h2>
  <div class="abs step-card" style="left:99px"><span class="step-number">1</span>Lorem ipsum dolor sit amet, consectetur adipiscing elit, sed do eiusmod tempor incididunt ut labore et dolore magna aliqua.</div>
  <div class="abs step-card" style="left:278px"><span class="step-number">2</span>Lorem ipsum dolor sit amet, consectetur adipiscing elit, sed do eiusmod tempor incididunt ut labore et dolore magna aliqua.</div>
  <div class="abs step-card" style="left:457px"><span class="step-number">3</span>Lorem ipsum dolor sit amet, consectetur adipiscing elit, sed do eiusmod tempor incididunt ut labore et dolore magna aliqua.</div>

  <footer>
    <h4 class="abs newsletter-title"><strong>News</strong><span>letter</span></h4>
    <div class="abs newsletter-input">Stay up to date with our latest news</div>
    <div class="abs subscribe-button">Subscribe</div>
    <div class="abs social-links" aria-label="Social links"><span></span><span></span><span></span><span></span><span></span></div>
    <div class="abs legal">
      <div>© 2015 name here. All Rights Reserved</div>
      <div class="links"><span>Privacy Notice</span><span>Legal</span><span>Site Map</span></div>
    </div>
  </footer>
</body>
</html>
```